Webpage design for a translation agancy

We need to update and modernize our current Wordpress webpage www.vindorelka.se. I am happy with the basics but there are definitely room for an update.
We are a translation agency providing translation services B2B. We supply translations to different industries. Law, HR, Medical, Financial, IT, Technical, Business. Our clients are mostly Swedish based companies.
We would like to see designs that:
- Increases our conversions
- Conveys reliance to our visitors/clients
- Keeps the framework on our current webpage (more or less)
- The quote bottom and quotation form is a crucial for our business. Drag and drop is a must.
-We'd like to keep the banner pics. One of them is our view from our office and the two others are local pictures from Stockholm/Sweden. The banner and the quote has to be integrated in the update.
-The design has to include designs for the whole webpage, landing page and all other pages.
/Tomas
Target Market(s)
Our target market is Swedish companies, b2b, operating in different industries. Law, Finance, Medical, IT, HR, Marketing, Engineering. Only B2B. Our typical buyer is a decision maker/ middle management.
Coding
Requirements
Must have
- - Conveys reliance to our visitors/clients
- - Our current Unique Selling Points
- - Keeps the framework on our current webpage (more or less)
- - The quote bottom and quotation form is a crucial for our business. One compeditor whom has a good solution for the quote form is, www.kelmarun.lv/en/
- -We'd like to keep the banner pics. One of them is our view from our office and the two others are local pictures from Stockholm/Sweden. The banner and the quote has to be integrated in the update.
- -The design has to include designs for the whole webpage, landing page and all other pages.
Nice to have
- Pretty much same color scales as today.

```html
<!DOCTYPE html>
<html lang="en">
<head>
<meta charset="utf-8">
<title>Vindorelka – Translation Agency</title>
<link href="https://fonts.googleapis.com/css2?family=Montserrat:wght@400;500;600;700&display=swap" rel="stylesheet">
<style>
:root{
  --blue:#2a9fe6;
  --teal:#1a9bcc;
  --purple:#7d3fd2;
  --ink:#2f2f2f;
  --text:#444;
  --grey:#f2f2f2;
  --lavender:#f6f0fc;
  --mint:#eff8fb;
  --card:#3a3a3a;
}
*{margin:0;padding:0;box-sizing:border-box}
html,body{width:1200px;height:1200px;overflow:hidden;background:#fff}
body{font-family:'Montserrat',sans-serif;color:var(--text)}
.stage{position:absolute;left:0;top:0;width:1500px;height:1500px;transform:scale(.8);transform-origin:0 0}
.page{position:absolute;left:495px;top:0;width:510px;height:1500px;background:#fff}
.abs{position:absolute}
.topbar{left:0;top:0;width:510px;height:13px;background:var(--blue);color:#fff;font-size:5px;font-weight:500}
.topbar span{position:absolute;top:4px}
.navbar{left:0;top:13px;width:510px;height:27px;background:#f1f1f1}
.logo{font-size:15px;font-weight:600;color:#555;letter-spacing:-.3px}
.logo b{color:#333}
.nav a{position:absolute;top:11px;font-size:5px;color:var(--blue);text-decoration:none}
.hero{left:0;top:40px;width:510px;height:227px}
.hero h1{position:absolute;left:0;width:510px;top:104px;text-align:center;color:#fff;font-size:14px;font-weight:700}
.hero p{position:absolute;left:90px;width:330px;top:124px;text-align:center;color:#fff;font-size:6.4px;line-height:10px;font-weight:500}
.btn{position:absolute;background:var(--blue);color:#fff;font-weight:600;text-align:center}
.btn.purple{background:var(--purple)}
.dropdown{left:234px;top:40px;width:150px;height:60px;background:#fff;font-size:5px;color:var(--blue);box-shadow:0 1px 3px rgba(0,0,0,.2)}
.dropdown div{position:absolute;line-height:8.6px}
.stat{left:49px;top:287px;width:200px;height:47px;border:2px solid var(--teal);color:var(--teal);font-weight:700}
.ask{left:262px;top:287px;width:200px;height:47px;border:2px solid var(--purple)}
h2{position:absolute;font-size:13.5px;font-weight:700;color:var(--ink)}
h3{position:absolute;font-size:9px;font-weight:700;color:var(--teal)}
.copy{position:absolute;left:47px;width:418px;font-size:5.6px;line-height:9.3px;color:#444}
.process{left:0;top:634px;width:510px;height:114px;background:var(--grey)}
.step{position:absolute;top:0;height:114px;text-align:center}
.step .dot{position:absolute;left:50%;top:15px;width:43px;height:43px;margin-left:-21.5px;border-radius:50%;background:var(--purple)}
.step .stem{position:absolute;left:50%;top:58px;width:2px;height:24px;margin-left:-1px;background:#666}
.step .end{position:absolute;left:50%;top:80px;width:5px;height:5px;margin-left:-2.5px;border-radius:50%;background:#666}
.step .lbl{position:absolute;left:0;width:100%;top:92px;font-size:6.3px;font-weight:600;color:var(--purple)}
.divider{position:absolute;top:0;width:1px;height:114px;background:#ddd}
.industry{left:0;top:748px;width:510px;height:187px;background:var(--lavender)}
.ind{position:absolute;width:130px}
.ind h4{font-size:8.5px;font-weight:500;color:var(--purple);margin-left:22px;line-height:14px}
.ind svg{position:absolute;left:0;top:-1px}
.ind p{font-size:5.5px;line-height:8.6px;color:#333;margin-top:4px}
.why{left:0;top:935px;width:510px;height:208px;background:var(--mint)}
.wbox{position:absolute;width:203px;height:68px;border:2px solid var(--teal);background:#fff}
.wbox .ico{position:absolute;left:8px;top:8px;width:26px;height:26px;border-radius:50%;background:#eef1f3}
.wbox h5{position:absolute;left:40px;top:8px;font-size:9px;font-weight:500;color:var(--teal)}
.wbox p{position:absolute;left:41px;top:25px;width:155px;font-size:5px;line-height:10px;color:#333}
.news{position:absolute;width:134px;height:146px;top:1179px}
.news .ph{height:77px;background:linear-gradient(135deg,#e9eef4,#d9b48e 55%,#c4946b)}
.news .body{height:69px;background:var(--card);color:#fff;padding:9px 8px}
.news h6{font-size:7px;font-weight:500}
.news p{font-size:5px;line-height:10px;margin-top:3px;font-weight:500}
.news small{display:block;font-size:5.5px;font-weight:600;margin-top:2px}
.clients{left:0;top:1343px;width:510px;height:47px;background:#f4f4f4;color:#777}
.clients span{position:absolute;top:19px;font-size:7.5px;font-weight:600}
.footer{left:0;top:1390px;width:510px;height:110px;background:#f0f0f0;color:#333}
.footer .col{position:absolute;top:14px;font-size:5.5px;line-height:10.8px}
.footer .col b{display:block;font-size:5.6px;font-weight:700;margin-bottom:3px;line-height:8px}
.social{position:absolute;top:1449px;width:19px;height:19px;border-radius:50%}
</style>
</head>
<body>
<div class="stage">
<div class="page">

  <div class="abs topbar">
    <span style="left:329px">Interpreter</span>
    <span style="left:375px">Language ▾</span>
    <span style="left:411px">Request a quote</span>
  </div>

  <div class="abs navbar">
    <div class="abs logo" style="left:48px;top:4px"><b>vindorelka</b></div>
    <nav class="nav">
      <a style="left:170px">Home</a>
      <a style="left:198px">About Us</a>
      <a style="left:233px">Our Services ⌄</a>
      <a style="left:276px">Translation Solution</a>
      <a style="left:338px">Our Customers</a>
      <a style="left:387px">For Translator</a>
      <a style="left:433px">Contact</a>
    </nav>
  </div>

  <section class="abs hero">
    <svg width="510" height="227" style="position:absolute;left:0;top:0" role="img" aria-label="Banner photo of the office view in Stockholm">
      <defs><linearGradient id="heroShade" x1="0" y1="0" x2="0" y2="1"><stop offset="0" stop-color="#3d3d40"/><stop offset=".5" stop-color="#55565a"/><stop offset="1" stop-color="#2e2f33"/></linearGradient></defs>
      <polygon points="0,0 510,0 510,167 255,227 0,167" fill="url(#heroShade)"/>
    </svg>
    <h1>We Transplate Millions Of Words Every Year</h1>
    <p>Lorem Ipsum is simply dummy text of the printing and typesetting industry. Lorem Ipsum has been the industry's standard dummy text ever since the 1500s</p>
    <div class="btn" style="left:205px;top:150px;width:103px;height:22px;line-height:22px;font-size:7.5px">Request For Quotation</div>
  </section>

  <div class="abs dropdown">
    <div style="left:5px;top:5px">Industry Specialization ›<br>Project<br>Graphic Services / DTP<br>Proof<br>Interpreter<br>Our translator</div>
    <div style="left:80px;top:5px">Industrial / Machinery<br>Law<br>IT / Web<br>Financial<br>Market<br>Medicine</div>
  </div>

  <div class="abs stat">
    <div class="abs" style="left:4px;top:2px;font-size:35px;letter-spacing:-.5px">98%</div>
    <div class="abs" style="left:99px;top:5px;font-size:7.5px;font-weight:600">Customer Satisfaction</div>
    <div class="abs" style="left:98px;top:11px;font-size:25px">In 2016</div>
  </div>
  <div class="abs ask">
    <div class="abs" style="left:3px;top:4px;width:195px;font-size:7.6px;font-weight:700;color:var(--purple);line-height:10px">If you have questions or? Something you need help with?</div>
    <div class="abs" style="left:3px;top:29px;font-size:4.6px;font-weight:700;color:#333">Click here to answer? We are with you again.</div>
    <div class="btn purple" style="left:131px;top:21px;width:63px;height:20px;line-height:20px;font-size:5.6px">For Question</div>
  </div>

  <h2 style="left:47px;top:344px">Vindorelka translation agency</h2>
  <p class="copy" style="top:367px">Vindorelka is a translation agency offering translations of the highest quality. We are a valued partner who has helped companies and institutions with language services for over 10 years. What characterizes us is above all our high level of service combined with a price awareness. We as a translation agency is additionally certified according to ISO 9001: 2008.</p>

  <h3 style="left:47px;top:403px">Our Services</h3>
  <p class="copy" style="top:417px">Our mission as a translation agency is to efficiently provide translation services with a focus on personalized service and expertise. Whether your translation in technical manuals, legal documents, annual reports or medical translation so we can help you.</p>
  <p class="copy" style="top:439px">Along with the most competent translator, we offer language services of the highest quality, while the translation companies working to save money for our customers.</p>

  <h3 style="left:47px;top:467px">The Best Translator</h3>
  <p class="copy" style="top:481px;width:420px">Vindorelka translation agency has a specialized and quality assured network of experienced linguists. The translators are not only very competent but they also have extensive experience in their respective disciplines. Our linguists are accustomed to working with deadlines and handle tough delivery requirements. All to ensure maximum quality and service.</p>
  <p class="copy" style="top:514px;left:49px">Each mission requires not only the right translator in terms of language combination, but also in terms of the type of text, subject, text, target audience, and format.</p>

  <h3 style="left:49px;top:542px">Translation agency with technology solutions</h3>
  <p class="copy" style="top:556px;left:49px">Vindorelka works with translation technologies that improve our ability to translation agency to shorten our delivery times while improving translation quality.</p>
  <p class="copy" style="top:578px;left:49px">Our tools allow us to create conditions for consistent terminology across the enterprise. It is useful for large organizations, but also for smaller companies with recurring texts. Our goal as a translation agency is to facilitate the process for our customers. We always try to find the simplest technical solutions for you and your business.</p>
  <p class="copy" style="top:610px;left:49px">Contact us to find out how we can help you.</p>

  <section class="abs process">
    <div class="step" style="left:48px;width:100px"><div class="dot"><svg width="43" height="43"><rect x="14" y="11" width="15" height="20" rx="1.5" fill="none" stroke="#fff" stroke-width="1.4"/><path d="M17 17h9M17 21h9M17 25h9" stroke="#fff" stroke-width="1.2"/></svg></div><div class="stem"></div><div class="end"></div><div class="lbl">Request a quote</div></div>
    <div class="divider" style="left:156px"></div>
    <div class="step" style="left:152px;width:100px"><div class="dot"><svg width="43" height="43"><circle cx="19" cy="19" r="6.5" fill="none" stroke="#fff" stroke-width="2"/><path d="M24 24l6 6" stroke="#fff" stroke-width="2.6" stroke-linecap="round"/></svg></div><div class="stem"></div><div class="end"></div><div class="lbl">We analyze</div></div>
    <div class="divider" style="left:252px"></div>
    <div class="step" style="left:256px;width:100px"><div class="dot"><svg width="43" height="43"><path d="M11 19l10.5-8 10.5 8v12H11z" fill="none" stroke="#fff" stroke-width="1.4"/><path d="M11 19l10.5 7 10.5-7" fill="none" stroke="#fff" stroke-width="1.4"/></svg></div><div class="stem"></div><div class="end"></div><div class="lbl">You get a free quote</div></div>
    <div class="divider" style="left:356px"></div>
    <div class="abs" style="left:374px;top:28px;width:15px;height:18px;border:1px solid #4b7fc4;background:#fff"></div>
    <div class="abs" style="left:394px;top:35px;width:11px;height:11px;border-radius:50%;border:1px solid #555"></div>
    <div class="abs" style="left:408px;top:37px;font-size:3.6px;line-height:4.5px;color:#555">Member of the<br>translators guild</div>
    <div class="btn purple" style="left:373px;top:64px;width:77px;height:20px;line-height:20px;font-size:5.6px">Request For Quotation</div>
  </section>

  <section class="abs industry">
    <h2 style="left:49px;top:21px">We can be your industry</h2>
    <div class="ind" style="left:52px;top:60px"><svg width="18" height="16"><circle cx="9" cy="8" r="5" fill="none" stroke="#7d3fd2" stroke-width="3" stroke-dasharray="2.2 1.7"/><circle cx="9" cy="8" r="2" fill="#7d3fd2"/></svg><h4>Industrial / Machinery</h4><p>Translation of service and installation instructions in the industrial, electrical and automotive engineering, etc.</p></div>
    <div class="ind" style="left:194px;top:60px"><svg width="18" height="16"><path d="M3 14h11M8 3l6 5-2 2-6-5z" fill="#7d3fd2" stroke="#7d3fd2" stroke-width="1.3"/></svg><h4>Law</h4><p>Translation of legal documents, contracts, judgments, insurance and authorized documents, etc.</p></div>
    <div class="ind" style="left:329px;top:60px"><svg width="18" height="16"><rect x="1" y="5" width="16" height="6" rx="3" fill="none" stroke="#7d3fd2" stroke-width="1.3"/></svg><h4>IT / Web</h4><p>Translation of software, websites, technical specifications, manuals, CMS and IT systems, etc.</p></div>
    <div class="ind" style="left:52px;top:124px"><svg width="18" height="16"><path d="M1 6l8-4 8 4z" fill="#7d3fd2"/><path d="M3 7v6M7 7v6M11 7v6M15 7v6" stroke="#7d3fd2" stroke-width="1.6"/><rect x="1" y="13" width="16" height="2" fill="#7d3fd2"/></svg><h4>Financial</h4><p>Translation of annual reports, quarterly reports, fund descriptions, market reports, prospectuses, etc.</p></div>
    <div class="ind" style="left:194px;top:124px"><svg width="18" height="16"><circle cx="9" cy="7" r="4" fill="#7d3fd2"/><rect x="7.3" y="11" width="3.4" height="3" fill="#7d3fd2"/><path d="M2 7h2M14 7h2M9 0v2" stroke="#7d3fd2"/></svg><h4>Market</h4><p>Translation of the market requires that your message is conveyed in a proper manner so as to reach out to your audience.</p></div>
    <div class="ind" style="left:329px;top:124px"><svg width="18" height="16"><rect x="1" y="4" width="16" height="11" fill="#7d3fd2"/><path d="M9 6.5v6M6 9.5h6" stroke="#fff" stroke-width="1.6"/><rect x="6" y="1.5" width="6" height="3" fill="none" stroke="#7d3fd2"/></svg><h4>Medicine</h4><p>Translation of research papers, publications, SPC, package leaflets, manuals, training and marketing materials, etc.</p></div>
  </section>

  <section class="abs why">
    <h2 style="left:49px;top:15px">Why Us ?</h2>
    <div class="wbox" style="left:47px;top:44px"><div class="ico"></div><h5>Quality</h5><p>We focus on high quality in all aspects of the translation process, from project management, translation, revision to delivery.</p></div>
    <div class="wbox" style="left:260px;top:44px"><div class="ico"></div><h5>Delivery</h5><p>Our goal is that in all our projects maintain the best possible delivery time and deliver the format that saves our customers time.</p></div>
    <div class="wbox" style="left:47px;top:123px"><div class="ico"></div><h5>Competence</h5><p>As a translation agency we have demands on us to always be one step ahead. We only work with the most competent project managers, translators and proofreaders</p></div>
    <div class="wbox" style="left:260px;top:123px"><div class="ico"></div><h5>Secrecy</h5><p>We treat all our customers' assignments and documents with high standards of security and confidentiality.</p></div>
  </section>

  <h2 style="left:49px;top:1157px">Our News</h2>
  <article class="news" style="left:47px"><div class="ph" role="img" aria-label="Photo of a business handshake"></div><div class="body"><h6>Untranstable word</h6><p>Language reflects an entire culture and language is built up in different ways with different peculiarities.</p><small>2017 February 02</small></div></article>
  <article class="news" style="left:188px"><div class="ph" role="img" aria-label="Photo of a business handshake"></div><div class="body"><h6>New Year new word</h6><p>Language reflects an entire culture and language is built up in different ways with different peculiarities.</p><small>2017 January 09</small></div></article>
  <article class="news" style="left:330px"><div class="ph" role="img" aria-label="Photo of a business handshake"></div><div class="body"><h6>Seen then approached Lucia..</h6><p>Language reflects an entire culture and language is built up in different ways with different peculiarities.</p><small>2016 December 05</small></div></article>

  <div class="abs clients">
    <span style="left:50px">Skyvandra</span>
    <span style="left:120px">Hallbeck &amp; Co</span>
    <span style="left:192px">Norrvik Invest</span>
    <span style="left:250px">Brantholm Media</span>
    <span style="left:336px">Solresa</span>
    <span style="left:408px">Kvarnlund</span>
  </div>

  <footer class="abs footer">
    <div class="abs logo" style="left:48px;top:14px;font-size:12px"><b>vindorelka</b></div>
    <div class="col" style="left:49px;top:36px;width:100px;font-size:5px;line-height:8.8px">Phasellus sed lectus id massa euismod tincidunt semper et odio. Etiam lobortis ipsum risus, vitae rhoncus est rhoncus vel. Ut malesuada euismod massa, vitae ipsum risus.</div>
    <div class="col" style="left:161px"><b>Vindorelka Translation Agency</b>Request a quote<br>Contact<br>About us<br>VAT: SE559012345601</div>
    <div class="col" style="left:268px"><b>TRANSLATION SERVICES</b>technical translations<br>legal translations<br>financial translations<br>medical translations</div>
    <div class="col" style="left:368px;line-height:9.4px"><b>Contact Detail</b>Lindgatan 17,<br>SE-112 40 Stockholm<br>+46 (0) 8 555 01 37</div>
    <div class="abs" style="left:49px;top:93px;font-size:4px;color:#555">© 2017 Vindorelka. all rights reserved</div>
  </footer>
  <div class="social" style="left:368px;background:#3b5a9a"></div>
  <div class="social" style="left:393px;background:#2aa3e6"></div>
  <div class="social" style="left:418px;background:#1d77b0"></div>

</div>
</div>
</body>
</html>
```